Harbor Ledger BC

I have a baseline business card that I would like to spruce up!

I actually like this business card. I just want to find a way to have all the information below on it and it too look balanced and professional.

Target Market(s)

Small to medium sized companies - Health Insurance Consulting

Industry/Entity Type

Health Insurance

Contact Information for Business Card

The information I would like included on the business card is:

- Harbor Ledger Pacific Title and logo
- Dana Whitlow
- Business title: Principal
- 4312 Alder Crest Rd Suite C-215 Fernvale, WA 98172
- Employee Benefits Consulting & (Wellness Consulting) optional
- dana@harborledgerpac.com
- cell: 425-731-4062

Font styles to use
Other font styles liked:
• I like the font it is currently in but am open to others.

Requirements
Must have
• I like the logo and the color scheme. I even like the layout. I just need to fine tune it!

```html
<!DOCTYPE html>
<html lang="en">
<head>
<meta charset="utf-8">
<title>Harbor Ledger Pacific – Business Card</title>
<link href="https://fonts.googleapis.com/css2?family=Lato:wght@300;400;700&display=swap" rel="stylesheet">
<style>
  :root {
    --brand-green: #0b8450;
    --brand-green-dark: #087045;
    --ink: #1c1c1c;
    --ink-soft: #555555;
    --paper: #ffffff;
    --backdrop: #e9ebea;
  }
  * { box-sizing: border-box; margin: 0; padding: 0; }
  html, body {
    width: 1200px; height: 900px; overflow: hidden;
    background: var(--backdrop);
    font-family: "Lato", Arial, sans-serif;
  }
  .canvas { position: relative; width: 1200px; height: 900px; }

  .card {
    position: absolute; left: 250px;
    width: 700px; height: 400px;
    box-shadow: 0 6px 18px rgba(0,0,0,0.18);
    overflow: hidden;
  }
  .card--back { top: 35px; background: var(--brand-green); color: var(--paper); }
  .card--front { top: 465px; background: var(--paper); color: var(--ink); }
  .card--front::after {
    content: ""; position: absolute; left: 0; right: 0; bottom: 0;
    height: 12px; background: var(--brand-green);
  }

  /* wordmark lockup */
  .lockup { position: absolute; display: flex; align-items: center; }
  .lockup__mark { width: 74px; height: 74px; border-radius: 50%; flex: none; }
  .lockup__name {
    margin-left: 16px; font-weight: 400; font-size: 27px;
    letter-spacing: 1px; text-transform: uppercase; line-height: 1;
  }
  .lockup__divider { width: 1px; height: 86px; margin: 0 16px 0 22px; }
  .lockup__service { font-weight: 300; font-size: 16px; line-height: 1.05; }

  .card--back .lockup { left: 120px; top: 118px; }
  .card--back .lockup__mark { background: var(--paper); }
  .card--back .lockup__name { color: var(--paper); }
  .card--back .lockup__divider { background: rgba(255,255,255,0.7); }
  .card--back .lockup__service { color: var(--paper); }

  .tagline {
    position: absolute; left: 0; right: 0; top: 275px;
    text-align: center; font-size: 20px; font-weight: 400; letter-spacing: 0.3px;
  }

  .card--front .lockup { left: 50px; top: 48px; }
  .card--front .lockup__mark { background: var(--brand-green); }
  .card--front .lockup__name { color: var(--ink); }
  .card--front .lockup__divider { background: #777; }
  .card--front .lockup__service { color: var(--ink-soft); }

  .contact { position: absolute; left: 55px; top: 185px; font-size: 19px; line-height: 1.3; }
  .contact__address { margin-bottom: 16px; }
  .contact__row { display: flex; align-items: center; }
  .contact__icon { width: 18px; height: 18px; margin-right: 12px; flex: none; }

  .person { position: absolute; left: 430px; top: 290px; }
  .person__name { color: var(--brand-green); font-size: 30px; font-weight: 400; }
  .person__title { font-size: 19px; font-weight: 700; color: var(--ink); }
</style>
</head>
<body>
<main class="canvas">

  <section class="card card--back" aria-label="Card back">
    <div class="lockup">
      <span class="lockup__mark" aria-hidden="true"></span>
      <span class="lockup__name">Harbor Ledger Pacific</span>
      <span class="lockup__divider" aria-hidden="true"></span>
      <span class="lockup__service">Employee<br>Benefits<br>Services</span>
    </div>
    <p class="tagline">Employee Benefits Consulting &bull; Wellness Consulting</p>
  </section>

  <section class="card card--front" aria-label="Card front">
    <div class="lockup">
      <span class="lockup__mark" aria-hidden="true"></span>
      <span class="lockup__name">Harbor Ledger Pacific</span>
      <span class="lockup__divider" aria-hidden="true"></span>
      <span class="lockup__service">Employee<br>Benefits<br>Services</span>
    </div>

    <address class="contact" style="font-style:normal">
      <p class="contact__address">4312 Alder Crest Rd Suite C-215<br>Fernvale, WA 98172</p>
      <p class="contact__row">
        <svg class="contact__icon" viewBox="0 0 18 18" aria-label="Cell">
          <rect x="4.5" y="1" width="9" height="16" rx="1.5" fill="none" stroke="#0b8450" stroke-width="1.6"/>
          <rect x="6" y="3" width="6" height="9" fill="#0b8450"/>
          <circle cx="9" cy="14.5" r="1" fill="#0b8450"/>
        </svg>
        425-731-4062
      </p>
      <p class="contact__row">
        <svg class="contact__icon" viewBox="0 0 18 18" aria-label="Email">
          <rect x="1" y="4" width="16" height="11" fill="#0b8450"/>
          <path d="M1 4 L9 10.5 L17 4" fill="none" stroke="#ffffff" stroke-width="1.3"/>
        </svg>
        dana@harborledgerpac.com
      </p>
    </address>

    <div class="person">
      <p class="person__name">Dana Whitlow</p>
      <p class="person__title">Principal</p>
    </div>
  </section>

</main>
</body>
</html>
```